Roofing Contractor website

I currently have a website. But I would like it redesigned. Here is my website:
www.brambletopshingle.co

I want to try and mimic the look of another website: www.vestapixelworks.com

For legal reasons I don’t want to copy it 100%, but I would like to copy it as much as possible because I like the look and simplicity of this website. We have similar colors. My company colors are black, red and white.

I am not very good at web design, but I am good enough to go into front page and change some text and images if the main design is already created for me. I am looking for someone to basically create 95% of this front page site for me, and I can go in and tweak some of the wording and images later.

My current website already has SEO work done. So I do not want to lose the work that is done already because I am currently ranked very well in my area. I just want the design of my site to change but not lose any seo rankings.

I attached some wording id like to replace from the vesta pixelworks website. But this is NOT complete. Just some notes I wrote down. We can get together to make this more complete later.

The most important things to me is that I do not lose SEO and the overall look and design is similar to vesta pixelworks website but its designed for my brambletop shingle website.

Coding

```html
<!DOCTYPE html>
<html lang="en">
<head>
<meta charset="utf-8">
<title>Brambletop Shingle – Roofing Contractor Website</title>
<link href="https://fonts.googleapis.com/css2?family=Bebas+Neue&family=Source+Sans+3:wght@400;600;700&display=swap" rel="stylesheet">
<style>
:root{
  --board:#1a1a1a;
  --page:#000000;
  --panel:#14161f;
  --red:#e50914;
  --white:#ffffff;
  --muted:#c9ccd4;
  --line:#3a3d48;
  --paper:#f4f4f4;
  --ink:#1c1c1c;
}
*{margin:0;padding:0;box-sizing:border-box}
html,body{width:1200px;height:1200px;overflow:hidden;background:var(--board)}
body{font-family:"Source Sans 3",Arial,sans-serif;color:var(--white)}
.stage{position:absolute;left:0;top:0;width:1932px;height:1932px;transform:scale(0.62112);transform-origin:0 0}
.page{position:absolute;background:var(--page)}
.page-home{left:307px;top:38px;width:645px;height:1855px}
.page-inner{left:980px;top:38px;width:645px;height:1499px}
.abs{position:absolute}
.display{font-family:"Bebas Neue",Impact,sans-serif;font-size:22px;line-height:23px;letter-spacing:.2px;font-weight:400}
.accent{color:var(--red)}
.body{font-size:8px;line-height:10.3px;text-align:justify}
.btn{position:absolute;background:var(--red);color:var(--white);font-size:8.5px;font-weight:700;display:flex;align-items:center;justify-content:center;border-radius:2px}
.btn-outline{position:absolute;border:1px solid var(--red);color:var(--white);font-size:8px;font-weight:600;display:flex;align-items:center;justify-content:center;border-radius:2px}
.photo{position:absolute}
.brand{position:absolute;display:flex;align-items:center;gap:4px}
.brand-dot{width:14px;height:14px;border-radius:50%;background:var(--red)}
.brand-name{font-size:7px;font-weight:700;color:var(--red);line-height:8px;width:60px}
.nav{position:absolute;left:279px;top:36px;font-size:8px;display:flex;gap:9px}
.badge{position:absolute;top:392px;width:70px;height:14px;background:#3b3b3b;border-radius:2px}
.rating{position:absolute;top:332px;display:flex;align-items:center;gap:5px}
.rating-score{font-size:20px;font-weight:700}
.rating-meta{font-size:6px;line-height:7px}
.stars{color:#f5b50a;font-size:7px;letter-spacing:1px}
.review{position:absolute;top:713px;width:184px;height:129px;background:var(--panel);padding:22px 15px}
.review-head{display:flex;gap:6px;align-items:center;font-size:5.5px;line-height:7px}
.avatar{width:11px;height:11px;border-radius:50%;background:#5a6070}
.review-name{font-weight:700}
.review .stars{font-size:9px;margin:6px 0 8px}
.review-text{font-size:5.5px;line-height:7.5px}
.source-dot{position:absolute;right:15px;top:24px;width:10px;height:10px;border-radius:50%;border:2px solid #8a8f9c}
.pager{position:absolute;width:22px;height:22px;border-radius:50%;border:1px solid #777;display:flex;align-items:center;justify-content:center}
.service-list{position:absolute;left:305px;top:1360px;width:253px;list-style:none;font-size:8px;color:var(--ink)}
.service-list li{height:20.5px;border-bottom:1px solid #d4d4d4;display:flex;align-items:center;gap:8px;padding-left:3px}
.tick{color:var(--red);font-size:8px;font-weight:700}
.step{position:absolute;left:61px;width:251px;font-size:8px;line-height:10.3px;border-bottom:1px solid #8a8a8a;padding:0 0 3px 18px}
.step::before{content:"";position:absolute;left:0;top:3px;width:6px;height:6px;background:var(--red)}
.step b{display:block}
.field{position:absolute;left:362px;width:203px;height:21px;background:#000;font-size:7.5px;color:#aaa;padding-left:8px;display:flex;align-items:center}
.article{position:absolute;top:995px;width:174px;height:186px;border:1px solid #dcdcdc;border-radius:6px;padding:112px 11px 0;color:var(--ink)}
.article h4{font-size:7.5px;line-height:10px;font-weight:700}
.article p{font-size:6px;line-height:7.5px;margin-top:8px;color:#555}
.foot-col{position:absolute;top:1285px}
.foot-col h5{font-family:"Bebas Neue",Impact,sans-serif;font-size:17px;font-weight:400;margin-bottom:16px}
.foot-col li{list-style:none;font-size:7.5px;height:20.5px}
.contact-row{display:flex;gap:10px;align-items:center}
</style>
</head>
<body>
<div class="stage">

  <!-- HOME PAGE -->
  <section class="page page-home">
    <div class="brand" style="left:53px;top:16px">
      <span class="brand-dot"></span><span class="brand-name">BRAMBLETOP SHINGLE</span>
    </div>
    <nav class="nav"><span>Home</span><span>About Us</span><span>Contact</span></nav>
    <div class="abs" style="left:452px;top:33px;display:flex;gap:6px;align-items:center;font-size:8px">
      <svg width="6" height="11" viewBox="0 0 6 11"><rect x="0.5" y="0.5" width="5" height="10" rx="1" fill="none" stroke="#e50914"/></svg>555-014-2290
    </div>
    <div class="btn" style="left:532px;top:31px;width:61px;height:18px">Schedule</div>

    <div class="photo" role="img" aria-label="Roofer in red shirt inspecting shingles on a roof" style="left:32px;top:61px;width:581px;height:291px;background:linear-gradient(180deg,rgba(0,0,0,0) 40%,#000 100%),linear-gradient(90deg,#1b1d22 0%,#3d3f44 45%,#55504b 70%,#3a3a3c 100%)"></div>
    <h1 class="abs display" style="left:52px;top:142px">THE BEST ROOFING<br>CONTRACTORS IN <span class="accent">MIDLOTHIAN, TX</span></h1>
    <p class="abs body" style="left:52px;top:197px;width:261px">Welcome to Brambletop Shingle Co. – Your Premier Roofing Contractors in Midlothian, Texas. Our expert team is dedicated to delivering top-notch roofing services, ensuring durability, and enhancing the resilience of homes in the heart of Texas. From roof installations to repairs, trust Brambletop Shingle Co. for unmatched quality and craftsmanship. Explore our range of services and experience roofing excellence tailored for Midlothian living.</p>
    <div class="btn" style="left:54px;top:288px;width:67px;height:17px">Get Started</div>

    <div class="rating" style="left:53px"><span class="rating-score">5,0</span><div class="rating-meta"><div style="font-size:7px;color:#7fb0ff">Findly</div><div class="stars">★★★★★</div>Five Star Customer Rating</div></div>
    <div class="rating" style="left:159px"><span class="rating-score">5,0</span><div class="rating-meta"><div style="font-size:7px;color:#7fb0ff">Circlebook</div><div class="stars">★★★★★</div>Five Star Customer Rating</div></div>

    <span class="badge" style="left:53px"></span><span class="badge" style="left:151px"></span><span class="badge" style="left:242px"></span>
    <span class="badge" style="left:340px"></span><span class="badge" style="left:430px"></span><span class="badge" style="left:528px"></span>

    <div class="photo" role="img" aria-label="Aerial view of a stone house during roof replacement" style="left:52px;top:444px;width:260px;height:166px;border-radius:8px;background:linear-gradient(160deg,#4f5a3a,#7c7a6a 45%,#2c2d33 80%,#6a6e5c)"></div>
    <h2 class="abs display" style="left:332px;top:445px">AN EASY <span class="accent">STRESS-FREE</span> EXPERIENCE</h2>
    <p class="abs body" style="left:332px;top:476px;width:261px">Investing in a new roof is a big deal, and you want a roofing company that's got your back. At Brambletop Shingle Co., we're not just about top warranties and durable materials – we're about making you feel confident throughout the whole process. Your money, time, and home matter, and we understand that. Our team brings a friendly, consultative vibe, ensuring you're in the loop and comfortable with every decision. Trust us for your roofing needs in Midlothian, Texas, and all around North Texas – we're here to make your roofing experience as stress-free as possible.</p>
    <div class="btn" style="left:335px;top:589px;width:60px;height:18px">Contact Us</div>

    <h2 class="abs display" style="left:0;width:645px;text-align:center;top:668px">HEAR FROM OUR HAPPY CLIENTS!</h2>
    <article class="review" style="left:40px"><span class="source-dot"></span>
      <div class="review-head"><span class="avatar"></span><div><div class="review-name">Marla Quinlan</div>January 26, 2024</div></div>
      <div class="stars">★★★★★</div>
      <p class="review-text">Dale is so easy to work with. Great communication and he did an amazing job on my Christmas lights . I recommend him to everyone!</p></article>
    <article class="review" style="left:231px"><span class="source-dot"></span>
      <div class="review-head"><span class="avatar"></span><div><div class="review-name">Dexter Holloway</div>January 21, 2024</div></div>
      <div class="stars">★★★★★</div>
      <p class="review-text">Dale is so easy to work with. Great communication and he did an amazing job on my Christmas lights . I recommend him to everyone!</p></article>
    <article class="review" style="left:421px"><span class="source-dot"></span>
      <div class="review-head"><span class="avatar" style="background:var(--red)"></span><div><div class="review-name">Rowan Fairbeck</div>January 19, 2024</div></div>
      <div class="stars">★★★★★</div>
      <p class="review-text">Great service!!</p></article>
    <div class="pager" style="left:280px;top:860px"><svg width="8" height="8" viewBox="0 0 8 8"><path d="M5 1L2 4l3 3" stroke="#fff" fill="none"/></svg></div>
    <div class="pager" style="left:344px;top:860px"><svg width="8" height="8" viewBox="0 0 8 8"><path d="M3 1l3 3-3 3" stroke="#fff" fill="none"/></svg></div>

    <div class="abs" style="left:80px;top:920px;width:485px;height:1px;background:#1e1e1e"></div>

    <div class="abs" style="left:297px;top:950px;width:296px;height:208px;border:1px solid #3a3a3a"></div>
    <div class="photo" role="img" aria-label="Close-up of rolled hundred dollar bills" style="left:311px;top:962px;width:268px;height:183px;background:linear-gradient(135deg,#2a3038,#8c9a8e 45%,#c9c2a6 65%,#3a3f36)"></div>
    <div class="abs" style="left:54px;top:1002px;width:296px;height:208px;border:1px solid var(--red)"></div>
    <div class="abs" style="left:64px;top:1012px;width:278px;height:188px;background:var(--panel)"></div>
    <h2 class="abs display" style="left:86px;top:1036px">REFER A FRIEND TODAY AND<br>RECEIVE <span class="accent">$500</span></h2>
    <p class="abs body" style="left:86px;top:1096px;width:234px">The best compliment you can give is to tell all your friends and family about us! Our referral program allows you to earn an industry high $500 for every referral you send our way! Nobody else in the industry rewards and appreciates their clients the way we do! If you tell your friends about us, and they use us to replace their roof, we thank you in a huge way!</p>
    <div class="btn-outline" style="left:255px;top:1168px;width:64px;height:22px">Refer a friend</div>

    <div class="abs" style="left:33px;top:1248px;width:580px;height:386px;background:var(--white)"></div>
    <h2 class="abs display" style="left:55px;top:1268px;color:var(--ink)">COMPREHENSIVE ROOFING SERVICES FROM<br><span class="accent">BRAMBLETOP SHINGLE CO.</span></h2>
    <div class="photo" role="img" aria-label="Roofer working on shingles" style="left:87px;top:1333px;width:119px;height:146px;background:linear-gradient(160deg,#7d8a66,#8d9bb0 50%,#4a4b4a)"></div>
    <div class="photo" role="img" aria-label="Worker installing a gutter" style="left:211px;top:1333px;width:65px;height:69px;background:linear-gradient(160deg,#d8dde0,#6e7678)"></div>
    <div class="photo" role="img" aria-label="Crew member by a fence outdoors" style="left:211px;top:1408px;width:65px;height:71px;background:linear-gradient(160deg,#6d8a58,#b45a4f 60%,#5a5e52)"></div>
    <p class="abs body" style="left:296px;top:1331px;width:262px;color:var(--ink)">Discover the complete roofing experience with Brambletop Shingle Co. Our comprehensive services cover residential and commercial roofing,</p>
    <ul class="service-list">
      <li><span class="tick">✔</span>Expert roof repairs</li>
      <li><span class="tick">✔</span>Seamless gutter installations</li>
      <li><span class="tick">✔</span>Quality fencing solutions</li>
      <li><span class="tick">✔</span>Festive Christmas light installations</li>
    </ul>
    <p class="abs body" style="left:296px;top:1450px;width:262px;color:var(--ink)">Elevate your home or business with our skilled team, ensuring excellence in every project. Trust Brambletop Shingle Co. for all your roofing, exterior, and festive needs in Midlothian, Texas, and throughout DFW.</p>

    <div class="abs" style="left:33px;top:1532px;width:30px;height:241px;background:var(--panel)"></div>
    <div class="abs" style="left:583px;top:1532px;width:30px;height:241px;background:var(--panel)"></div>
    <div class="abs" style="left:86px;top:1532px;width:473px;height:241px;background:var(--panel)"></div>
    <div class="photo" role="img" aria-label="Roofer checking storm damaged shingles" style="left:109px;top:1581px;width:204px;height:138px;background:linear-gradient(150deg,#7a7c80,#5b5d62 55%,#3d3e42)"></div>
    <h3 class="abs display" style="left:333px;top:1579px;font-size:18px;line-height:18px">ROOF DAMAGE RECOVERY DUE TO<br>SEVERE WEATHER</h3>
    <p class="abs body" style="left:333px;top:1627px;width:203px">Mother Nature can be a powerful force, and Dallas / Ft. Worth is no stranger to severe weather. Even if it isn't an intense storm that causes damage to your house or property, sometimes all it takes is the right gust of wind for something to go wrong. If this ever happens — don't panic! Brambletop Shingle Co. is here to help you recover from any storm damage quickly and restore your home to great condition.</p>
    <div class="pager" style="left:280px;top:1789px"><svg width="8" height="8" viewBox="0 0 8 8"><path d="M5 1L2 4l3 3" stroke="#fff" fill="none"/></svg></div>
    <div class="pager" style="left:344px;top:1789px"><svg width="8" height="8" viewBox="0 0 8 8"><path d="M3 1l3 3-3 3" stroke="#fff" fill="none"/></svg></div>
  </section>

  <!-- INNER PAGE -->
  <section class="page page-inner">
    <div class="abs" style="left:51px;top:83px;width:300px;height:159px;background:var(--panel);border-radius:6px"></div>
    <h2 class="abs display" style="left:69px;top:102px">FREE ROOF INSPECTION<br>WITH <span class="accent">DRONE</span> TECHNOLOGY</h2>
    <p class="abs body" style="left:69px;top:159px;width:246px">Brambletop Shingle Co. is your premiere Roofing Contractors in Midlothian, Texas. However, no matter where you are located in DFW; whether it be Mansfield or Ft. Worth, we offer FREE roof inspections using a combination of the latest drone technology and physically climbing the roof for peace of mind for a real close look. Please find the calendar below and schedule our FREE, no obligation inspection.</p>
    <div class="photo" role="img" aria-label="Drone flying above a brick house" style="left:334px;top:46px;width:279px;height:212px;background:linear-gradient(180deg,#4f86d6 0%,#8fb5e6 50%,#7d7468 75%,#8a7c66 100%)"></div>

    <p class="abs body" style="left:61px;top:345px;width:251px;font-weight:700">When you call Brambletop Shingle Co. you'll get a thorough and comprehensive roof consultation right out of the gate. Our consultation process includes:</p>
    <div class="step" style="top:410px"><b>Step 1.</b>Let's connect for a detailed discussion about your requirements, budget, and expectations.</div>
    <div class="step" style="top:451px"><b>Step 2.</b>Experience a thorough on-site roof inspection featuring drone footage, detailed pictures, and a meticulous evaluation.</div>
    <div class="step" style="top:492px"><b>Step 3.</b>We'll provide a detailed explanation of our recommendations, sharing findings and accompanying pictures to guide you in moving forward confidently.</div>
    <div class="step" style="top:542px"><b>Step 4.</b>Explore all available options to address your roof concerns and make informed decisions that best suit your home.</div>

    <div class="abs" style="left:344px;top:334px;width:234px;height:255px;background:var(--panel);border-radius:5px"></div>
    <h2 class="abs display" style="left:344px;width:234px;text-align:center;top:361px">CONTACT US NOW!</h2>
    <div class="field" style="top:409px">Name</div>
    <div class="field" style="top:436px">Phone</div>
    <div class="field" style="top:463px">Email</div>
    <div class="field" style="top:501px">Services</div>
    <div class="btn" style="left:433px;top:533px;width:60px;height:20px">Contact Us</div>

    <div class="abs" style="left:51px;top:649px;width:542px;height:206px;background:var(--paper);border-radius:7px"></div>
    <div class="photo" role="img" aria-label="Owner with family outdoors" style="left:118px;top:663px;width:178px;height:178px;background:linear-gradient(160deg,#c9b89a,#7a6e5a 55%,#3e3a30)"></div>
    <p class="abs body" style="left:332px;top:666px;width:250px;color:#444">At Brambletop Shingle Co., we strike the perfect balance – small enough to provide your project with personalized attention and large enough to tackle projects of any size. While many industry giants assign project managers for customer interaction, we distinguish ourselves by having our owner intimately involved in every project phase. You're never far from a reassuring voice as we prioritize personal service, ensuring total customer satisfaction.</p>
    <div class="abs" style="left:332px;top:747px;font-size:8px;color:var(--ink);line-height:10px"><b>Dale Morrow</b><br>Owner</div>
    <div class="abs" style="left:518px;top:766px;width:60px;height:18px;border:1px solid #555;border-radius:2px;font-size:8px;color:var(--ink);display:flex;align-items:center;justify-content:center">Read More</div>

    <div class="abs" style="left:32px;top:896px;width:581px;height:356px;background:var(--white)"></div>
    <h2 class="abs display" style="left:32px;width:581px;text-align:center;top:925px;color:var(--ink)"><span class="accent">GLOBAL SPOTLIGHT:</span> LATEST ARTICLES FROM THE WORLD OF<br>DIGITAL AND ENTERTAINMENT</h2>
    <article class="article" style="left:56px"><h4>SkyDash Arcade an online game that combines excitement and strategy to win</h4><p>In the fascinating universe of online gaming, SkyDash Arcade stands out as an exciting option for enthusiasts.</p></article>
    <article class="article" style="left:240px"><h4>Discover the Benefits of LuckyLantern Games for Your Safe and Fun Online Betting</h4><p>Choosing a reliable betting environment is essential to ensure a safe and enjoyable experience. When it comes to</p></article>
    <article class="article" style="left:418px"><h4>The best betting strategies for heavyweight fights to successfully predict the results</h4><p>Sporting events always attract the attention of fans not only with exciting competitions, but also with the opportunity to profit. One of the most</p></article>
    <div class="btn" style="left:278px;top:1199px;width:88px;height:22px;font-size:8px">View All Articel</div>

    <div class="brand" style="left:51px;top:1285px">
      <span class="brand-dot"></span><span class="brand-name">BRAMBLETOP SHINGLE</span>
    </div>
    <div class="abs" style="left:51px;top:1338px;font-size:8px">Best Midlothian Roofer</div>
    <div class="abs" style="left:51px;top:1374px;font-size:8px">Folow us:</div>
    <span class="abs" style="left:52px;top:1396px;width:16px;height:16px;border-radius:50%;border:1px solid #777"></span>
    <span class="abs" style="left:74px;top:1396px;width:16px;height:16px;border-radius:50%;border:1px solid #777"></span>

    <div class="foot-col" style="left:238px"><h5>SERVICES</h5><ul><li>Roof Replacements</li><li>Roof Repairs</li><li>Gutters</li><li>Christmas Light Installation</li><li>Fencing</li></ul></div>
    <div class="foot-col" style="left:360px"><h5>QUICK LINK</h5><ul><li>Home</li><li>About Us</li><li>Services</li><li>Contact Us</li></ul></div>
    <div class="foot-col" style="left:482px"><h5>CONTACT US</h5><ul>
      <li class="contact-row"><svg width="9" height="12" viewBox="0 0 9 12"><rect x="1" y="0.5" width="7" height="11" rx="1.2" fill="none" stroke="#e50914"/></svg>555-014-2290</li>
      <li class="contact-row"><svg width="9" height="12" viewBox="0 0 9 12"><path d="M4.5 11.5S1 7 1 4.5a3.5 3.5 0 017 0C8 7 4.5 11.5 4.5 11.5z" fill="none" stroke="#e50914"/><circle cx="4.5" cy="4.5" r="1.2" fill="#e50914"/></svg>Midlothian, Texas</li>
      <li class="contact-row"><svg width="11" height="9" viewBox="0 0 11 9"><rect x="0.5" y="0.5" width="10" height="8" fill="none" stroke="#e50914"/><path d="M0.5 0.5l5 4 5-4" fill="none" stroke="#e50914"/></svg>Info@brambletopshingle.co</li>
    </ul></div>

    <div class="abs" style="left:32px;top:1460px;width:581px;height:1px;background:var(--line)"></div>
    <div class="abs" style="left:32px;width:581px;text-align:center;top:1469px;font-size:7.5px">Copyright 2023 © All rights Reserved.</div>
  </section>

</div>
</body>
</html>
```